Tovrimel Complete Stationery - Logo already designed

I already have the logo designed see attached. I need have a full set of stationary and business card designed for printing. I have attached an example of what I mean.

Please feel free to be creative. Also you can use the X in the logo by its self if you think it will work.

My details:

Name: Dorian Pelsett
Social media handles: @dorianpelsett
W: dorianpelsett.com
E: info@dorianpelsett.com
​P: 08 7349 5286
PO Box 3872, Wendlemore 6047
ABN 83 274 908 615

Target Market(s)

Anyone looking to be inspired.

Industry/Entity Type

Business

Font styles to use
Sans Serif

Colors
fbee3e
000000

Requirements
Must have
• My details:
• Name: Dorian Pelsett
• Social media handles: @dorianpelsett
• W: dorianpelsett.com
• E: info@dorianpelsett.com
• ​P: 08 7349 5286
• PO Box 3872, Wendlemore 6047
• ABN 83 274 908 615
Nice to have
• Something a little different
Should not have
• must not look tacky.

```html
<!DOCTYPE html>
<html lang="en">
<head>
<meta charset="utf-8">
<title>Tovrimel Stationery Set</title>
<link rel="stylesheet" href="https://fonts.googleapis.com/css2?family=Open+Sans:wght@400;600;800&display=swap">
<style>
  :root {
    --yellow: #fbbe14;
    --black: #0d0c0c;
    --ink: #222222;
    --muted: #6d6d6d;
    --paper: #ffffff;
    --backdrop: #ebeadc;
    --folder-top: #1c1b1b;
    --folder-bottom: #090808;
  }
  * { box-sizing: border-box; margin: 0; padding: 0; }
  html, body { width: 1200px; height: 900px; overflow: hidden; }
  body { background: var(--backdrop); font-family: "Open Sans", Arial, sans-serif; color: var(--ink); }
  .canvas { position: relative; width: 1200px; height: 900px; overflow: hidden; }

  .sheet { position: absolute; background: var(--paper); box-shadow: 0 2px 8px rgba(0,0,0,.12); overflow: hidden; }

  .wordmark { font-family: "Open Sans", Arial, sans-serif; font-weight: 800; letter-spacing: .02em; text-transform: uppercase; line-height: 1; display: inline-flex; align-items: center; gap: 6px; }
  .wordmark .mark-square { width: .7em; height: .7em; background: var(--yellow); display: inline-block; }

  /* header: black tab, wordmark, yellow rule */
  .brand-head { position: absolute; left: 0; right: 0; display: flex; align-items: center; }
  .brand-head .tab { width: 50px; height: 5px; background: var(--black); flex: none; }
  .brand-head .wordmark { color: var(--black); margin: 0 10px; flex: none; }
  .brand-head .rule { flex: 1; height: 4px; background: var(--yellow); margin-top: 14px; }

  .contact-row { display: flex; flex-wrap: wrap; gap: 4px 14px; color: var(--muted); }
  .contact-row span { display: inline-flex; align-items: center; gap: 4px; white-space: nowrap; }
  .contact-row svg { flex: none; }

  .foot-bars { position: absolute; left: 0; right: 0; bottom: 0; height: 10px; }
  .foot-bars .black { position: absolute; left: 0; bottom: 5px; width: 60px; height: 4px; background: var(--black); }
  .foot-bars .yellow { position: absolute; left: 62px; right: 0; bottom: 0; height: 4px; background: var(--yellow); }

  /* letterhead */
  .letterhead { left: 330px; top: 28px; width: 400px; height: 566px; }
  .letterhead .brand-head { top: 34px; }
  .letterhead .wordmark { font-size: 19px; }
  .letter-body { position: absolute; left: 56px; right: 44px; top: 100px; font-size: 7.4px; line-height: 1.55; color: #333; }
  .letter-body p { margin-bottom: 9px; text-align: justify; }
  .letterhead .contact-row { position: absolute; left: 30px; right: 24px; bottom: 26px; font-size: 7.5px; justify-content: space-between; }

  /* folder */
  .folder { left: 790px; top: 150px; width: 380px; height: 540px; background: linear-gradient(160deg, var(--folder-top), var(--folder-bottom)); }
  .folder .band { position: absolute; left: 0; right: 0; bottom: 0; height: 7px; background: var(--yellow); }
  .folder .decor { position: absolute; left: 0; top: 0; right: 0; bottom: 7px; }
  .folder .wordmark { position: absolute; right: 34px; bottom: 46px; color: #f4f4f4; font-size: 30px; }

  /* business cards */
  .card { width: 240px; height: 138px; }
  .card-back { left: 40px; top: 330px; background: var(--black); }
  .card-back .decor { position: absolute; inset: 0; }
  .card-back .wordmark { position: absolute; left: 0; right: 0; top: 48px; justify-content: center; color: #ffffff; font-size: 18px; }
  .card-back .site { position: absolute; left: 0; right: 0; top: 76px; text-align: center; color: var(--yellow); font-size: 7px; }
  .card-back .edge { position: absolute; left: 0; right: 0; bottom: 0; height: 3px; background: var(--yellow); }

  .card-front { left: 40px; top: 490px; }
  .card-front .decor { position: absolute; inset: 0; }
  .card-front .wordmark { position: absolute; left: 14px; top: 16px; color: var(--black); font-size: 13px; }
  .card-front .holder { position: absolute; right: 16px; top: 40px; text-align: right; }
  .card-front .name { color: var(--yellow); font-weight: 600; font-size: 10px; }
  .card-front .role { color: var(--muted); font-size: 6.5px; margin-bottom: 6px; }
  .card-front .details { color: var(--muted); font-size: 6px; line-height: 1.5; }
  .card-front .edge { position: absolute; left: 0; right: 0; bottom: 0; height: 3px; background: var(--yellow); }

  /* compliments slip */
  .slip { left: 330px; top: 632px; width: 440px; height: 220px; }
  .slip .brand-head { top: 28px; }
  .slip .wordmark { font-size: 15px; }
  .slip .contact-row { position: absolute; left: 16px; right: 16px; bottom: 28px; font-size: 8px; justify-content: space-between; }
</style>
</head>
<body>
<div class="canvas">

  <svg width="0" height="0" style="position:absolute" aria-hidden="true">
    <defs>
      <symbol id="icon-pin" viewBox="0 0 10 10"><circle cx="5" cy="5" r="5" fill="#fbbe14"/><path d="M5 2.2a1.8 1.8 0 0 1 1.8 1.8C6.8 5.4 5 7.8 5 7.8S3.2 5.4 3.2 4A1.8 1.8 0 0 1 5 2.2z" fill="#fff"/></symbol>
      <symbol id="icon-phone" viewBox="0 0 10 10"><circle cx="5" cy="5" r="5" fill="#fbbe14"/><path d="M3.3 2.6l1 1-.5.7c.3.7.9 1.3 1.6 1.6l.7-.5 1 1-.6.9C4.9 7.1 2.9 5.1 2.6 3.5z" fill="#fff"/></symbol>
      <symbol id="icon-mail" viewBox="0 0 10 10"><circle cx="5" cy="5" r="5" fill="#fbbe14"/><rect x="2.6" y="3.3" width="4.8" height="3.4" fill="#fff"/><path d="M2.6 3.3L5 5.2l2.4-1.9" stroke="#fbbe14" stroke-width=".6" fill="none"/></symbol>
      <symbol id="icon-social" viewBox="0 0 10 10"><circle cx="5" cy="5" r="5" fill="#fbbe14"/><circle cx="5" cy="5" r="2" fill="#fff"/></symbol>
      <symbol id="icon-web" viewBox="0 0 10 10"><circle cx="5" cy="5" r="5" fill="#fbbe14"/><circle cx="5" cy="5" r="2.4" fill="none" stroke="#fff" stroke-width=".7"/><path d="M2.6 5h4.8M5 2.6v4.8" stroke="#fff" stroke-width=".6"/></symbol>
    </defs>
  </svg>

  <!-- Letterhead -->
  <section class="sheet letterhead">
    <header class="brand-head">
      <span class="tab"></span>
      <span class="wordmark">Tovrimel</span>
      <span class="rule"></span>
    </header>
    <div class="letter-body">
      <p>Lorem Ipsum is simply dummy text of the printing and typesetting industry. Lorem Ipsum has been the industry's standard dummy text ever since the 1500s, when an unknown printer took a galley of type and scrambled it to make a type specimen book. It has survived not only five centuries, but also the leap into electronic typesetting, remaining essentially unchanged. It was popularised in the 1960s with the release of Letraset sheets containing Lorem Ipsum passages, and more recently with desktop publishing software including versions of Lorem Ipsum.</p>
      <p>It is a long established fact that a reader will be distracted by the readable content of a page when looking at its layout. The point of using Lorem Ipsum is that it has a more-or-less normal distribution of letters, as opposed to using 'Content here, content here', making it look like readable English. Many desktop publishing packages and web page editors now use Lorem Ipsum as their default model text, and a search for 'lorem ipsum' will uncover many web sites still in their infancy. Various versions have evolved over the years, sometimes by accident, sometimes on purpose (injected humour and the like).</p>
      <p>Contrary to popular belief, Lorem Ipsum is not simply random text. It has roots in a piece of classical Latin literature from 45 BC, making it over 2000 years old. A Latin professor looked up one of the more obscure Latin words, consectetur, from a Lorem Ipsum passage, and going through the cites of the word in classical literature, discovered the undoubtable source. The generated Lorem Ipsum is therefore always free from repetition, injected humour, or non-characteristic words etc.</p>
    </div>
    <div class="contact-row">
      <span><svg width="9" height="9"><use href="#icon-pin"/></svg>PO Box 3872, Wendlemore 6047</span>
      <span><svg width="9" height="9"><use href="#icon-phone"/></svg>08 7349 5286</span>
      <span><svg width="9" height="9"><use href="#icon-mail"/></svg>info@dorianpelsett.com</span>
      <span><svg width="9" height="9"><use href="#icon-social"/></svg>@dorianpelsett</span>
      <span><svg width="9" height="9"><use href="#icon-web"/></svg>dorianpelsett.com</span>
    </div>
    <div class="foot-bars"><span class="black"></span><span class="yellow"></span></div>
  </section>

  <!-- Presentation folder -->
  <section class="sheet folder">
    <div class="decor" role="img" aria-label="Large faint brand symbol decoration on the folder cover" style="background: linear-gradient(135deg, rgba(255,255,255,.05), rgba(255,255,255,0) 70%);"></div>
    <span class="wordmark">Tovrimel</span>
    <span class="band"></span>
  </section>

  <!-- Business card, back -->
  <section class="sheet card card-back">
    <div class="decor" role="img" aria-label="Faint brand symbol decoration on the card back" style="background: linear-gradient(120deg, rgba(255,255,255,.07), rgba(255,255,255,0) 45%);"></div>
    <span class="wordmark">Tovrimel</span>
    <p class="site">www.dorianpelsett.com</p>
    <span class="edge"></span>
  </section>

  <!-- Business card, front -->
  <section class="sheet card card-front">
    <div class="decor" role="img" aria-label="Faint grey brand symbol decoration on the card front" style="background: linear-gradient(120deg, rgba(0,0,0,.05), rgba(0,0,0,0) 50%);"></div>
    <span class="wordmark">Tovrimel</span>
    <div class="holder">
      <p class="name">Dorian Pelsett</p>
      <p class="role">Designation</p>
      <p class="details">Social media handles: @dorianpelsett<br>W: dorianpelsett.com<br>E: info@dorianpelsett.com<br>P: 08 7349 5286<br>PO Box 3872, Wendlemore 6047<br>ABN 83 274 908 615</p>
    </div>
    <span class="edge"></span>
  </section>

  <!-- Compliments slip -->
  <section class="sheet slip">
    <header class="brand-head">
      <span class="tab"></span>
      <span class="wordmark">Tovrimel</span>
      <span class="rule"></span>
    </header>
    <div class="contact-row">
      <span><svg width="9" height="9"><use href="#icon-pin"/></svg>PO Box 3872, Wendlemore 6047</span>
      <span><svg width="9" height="9"><use href="#icon-phone"/></svg>08 7349 5286</span>
      <span><svg width="9" height="9"><use href="#icon-mail"/></svg>info@dorianpelsett.com</span>
      <span><svg width="9" height="9"><use href="#icon-social"/></svg>@dorianpelsett</span>
      <span><svg width="9" height="9"><use href="#icon-web"/></svg>dorianpelsett.com</span>
    </div>
    <div class="foot-bars"><span class="black"></span><span class="yellow"></span></div>
  </section>

</div>
</body>
</html>
```